Harbour Fellows - community/social/support group for men needs a flyer

We need a flyer for our community group for display in GP clinics and other community services offices. Please refer to our website for design ideas: www.harbourfellows.org.au. We need it to be clean and simple to read.

Target Market(s)

Men 18+

Font styles to use
Serif

Colors
00a990

```html
<!DOCTYPE html>
<html lang="en">
<head>
<meta charset="utf-8">
<title>Harbour Fellows Flyer</title>
<link rel="stylesheet" href="https://fonts.googleapis.com/css2?family=Montserrat:wght@400;800&family=Roboto+Condensed:wght@400;500&display=swap">
<style>
  :root {
    --page-bg: #e4e4e4;
    --paper: #ffffff;
    --ink-dark: #1f1f1f;
    --ink-mid: #3f3f3f;
    --ink-text: #333333;
    --panel-light: #ebebeb;
    --or-grey: #5a5a5a;
    --photo-top: #6f8a4e;
    --photo-bottom: #b4606b;
  }
  * { box-sizing: border-box; margin: 0; padding: 0; }
  html, body {
    width: 1200px; height: 2400px; overflow: hidden;
    background: var(--page-bg);
  }
  .flyer {
    position: absolute; left: 50px; top: 422px;
    width: 1100px; height: 1556px;
    background: var(--paper);
    box-shadow: 0 10px 30px rgba(0,0,0,0.25);
    overflow: hidden;
    font-family: "Roboto Condensed", "Arial Narrow", sans-serif;
    color: var(--ink-text);
  }
  .top-band {
    position: absolute; left: 0; top: 0; width: 100%; height: 579px;
    background: var(--ink-dark);
  }
  .brand-name {
    position: absolute; left: 0; top: 150px; width: 100%;
    text-align: center; color: #fff;
    font-family: "Montserrat", sans-serif; font-weight: 400;
    font-size: 46px; letter-spacing: 2px;
  }
  .hero-photo {
    position: absolute; left: 47px; top: 232px; width: 1008px; height: 593px;
    background: linear-gradient(180deg, var(--photo-top) 0%, #8c7a5e 50%, var(--photo-bottom) 100%);
  }
  .tagline {
    position: absolute; left: 47px; top: 842px; width: 1008px; height: 71px;
    background: var(--ink-dark); color: #fff;
    font-family: "Montserrat", sans-serif; font-weight: 800;
    font-size: 40px; line-height: 71px; text-align: center; letter-spacing: 0.5px;
  }
  .intro {
    position: absolute; left: 47px; width: 1008px;
    font-size: 17px; line-height: 22px; text-align: center;
  }
  .intro.first { top: 954px; }
  .intro.second { top: 1042px; }
  .projects {
    position: absolute; left: 47px; top: 1136px; width: 1008px; height: 218px;
    background: var(--panel-light);
  }
  .projects-title {
    position: absolute; left: 27px; top: 20px;
    font-size: 21px; font-weight: 500; text-transform: uppercase; color: var(--ink-text);
  }
  .project {
    position: absolute; font-size: 21px; display: flex; align-items: center; gap: 10px;
    white-space: nowrap;
  }
  .project svg { width: 20px; height: 20px; }
  .contact {
    position: absolute; left: 46px; top: 1396px; width: 1011px; height: 134px;
  }
  .contact-site {
    position: absolute; left: 0; top: 0; width: 536px; height: 100%;
    background: var(--ink-dark);
  }
  .contact-social {
    position: absolute; left: 536px; top: 0; width: 475px; height: 100%;
    background: var(--ink-mid);
  }
  .contact-note {
    position: absolute; color: #fff; font-size: 21px; line-height: 31px; text-align: center;
  }
  .contact-site .contact-note { left: 20px; width: 500px; top: 26px; }
  .contact-social .contact-note { left: 55px; width: 400px; top: 26px; }
  .contact-url {
    position: absolute; top: 96px; height: 27px; line-height: 27px;
    background: #555; color: #fff; font-size: 19px; text-align: center; letter-spacing: 0.5px;
  }
  .contact-site .contact-url { left: 134px; width: 247px; }
  .contact-social .contact-url { left: 50px; width: 380px; background: #262626; }
  .or-divider {
    position: absolute; left: 500px; top: 40px; width: 72px; text-align: center;
    font-family: "Roboto Condensed", sans-serif; font-weight: 500;
    font-size: 56px; color: var(--or-grey);
  }
</style>
</head>
<body>
  <main class="flyer">
    <header class="top-band">
      <div class="brand-name">HARBOUR FELLOWS</div>
    </header>

    <div class="hero-photo" role="img" aria-label="Photo of three laughing men standing together outdoors with trees behind them"></div>

    <h1 class="tagline">SOCIAL. SUPPORT. MATESHIP. COMMUNITY.</h1>

    <p class="intro first">Harbour Fellows Inc. is a community group that supports the positive activity, engagement and inclusion of men in Melbourne's Dandenong Ranges.&nbsp; Our aim is to reduce the number of men who are socially disadvantaged, marginalised or isolated to become productive, active members of the local community.</p>

    <p class="intro second">We do this by providing opportunities for men (18 years+) to come together in open, non-judgemental, safe spaces and participate in a range of social activities that encourage new friendships, normalise help-seeking behaviours and link with local support services.</p>

    <section class="projects">
      <h2 class="projects-title">We run a number of projects each year, which currently include:</h2>
      <div class="project" style="left:27px;top:81px"><svg viewBox="0 0 20 20"><rect x="2" y="4" width="14" height="14" fill="none" stroke="#333" stroke-width="1.6"/><path d="M5 10 l4 4 l9 -11" fill="none" stroke="#333" stroke-width="1.8"/></svg>Dads and kids playgroup</div>
      <div class="project" style="left:27px;top:127px"><svg viewBox="0 0 20 20"><rect x="2" y="4" width="14" height="14" fill="none" stroke="#333" stroke-width="1.6"/><path d="M5 10 l4 4 l9 -11" fill="none" stroke="#333" stroke-width="1.8"/></svg>Games Night</div>
      <div class="project" style="left:27px;top:173px"><svg viewBox="0 0 20 20"><rect x="2" y="4" width="14" height="14" fill="none" stroke="#333" stroke-width="1.6"/><path d="M5 10 l4 4 l9 -11" fill="none" stroke="#333" stroke-width="1.8"/></svg>Yarning Circle (men's discussion group)</div>
      <div class="project" style="left:342px;top:81px"><svg viewBox="0 0 20 20"><rect x="2" y="4" width="14" height="14" fill="none" stroke="#333" stroke-width="1.6"/><path d="M5 10 l4 4 l9 -11" fill="none" stroke="#333" stroke-width="1.8"/></svg>GBTIQ+ social dinners</div>
      <div class="project" style="left:342px;top:127px"><svg viewBox="0 0 20 20"><rect x="2" y="4" width="14" height="14" fill="none" stroke="#333" stroke-width="1.6"/><path d="M5 10 l4 4 l9 -11" fill="none" stroke="#333" stroke-width="1.8"/></svg>Shared Services working bee's</div>
      <div class="project" style="left:689px;top:81px"><svg viewBox="0 0 20 20"><rect x="2" y="4" width="14" height="14" fill="none" stroke="#333" stroke-width="1.6"/><path d="M5 10 l4 4 l9 -11" fill="none" stroke="#333" stroke-width="1.8"/></svg>Guest speakers</div>
      <div class="project" style="left:689px;top:127px"><svg viewBox="0 0 20 20"><rect x="2" y="4" width="14" height="14" fill="none" stroke="#333" stroke-width="1.6"/><path d="M5 10 l4 4 l9 -11" fill="none" stroke="#333" stroke-width="1.8"/></svg>Annual men's gathering &amp; more.</div>
    </section>

    <footer class="contact">
      <div class="contact-site">
        <p class="contact-note">For a list of our current activities and to find our how you can get involved, please visit us online at:</p>
        <div class="contact-url">www.harbourfellows.org.au</div>
      </div>
      <div class="contact-social">
        <p class="contact-note">join our Fellows Feed page for<br>our latest updates:</p>
        <div class="contact-url">www.fellowsfeed.net/harbourfellowsAU/</div>
      </div>
      <div class="or-divider">OR</div>
    </footer>
  </main>
</body>
</html>
```